Laundromat washing machine soap instructions poster

I own a laundromat and need a poster explaining to my customers how to load the soap, bleach and fabric softener into our washing machines. I tried to make a poster on canva but it looks terrible. My Laundromat is called "Suds Harbor" and would like my logo to also be on the poster for branding. I would like the poster to use my blue logo colors to match my brand identity.
Under the photo please include the following text:
" *Please place pods inside the washer"
Thanks
Laundromat

```html
<!DOCTYPE html>
<html lang="en">
<head>
<meta charset="utf-8">
<title>Suds Harbor – Where does the soap go?</title>
<link rel="stylesheet" href="https://fonts.googleapis.com/css2?family=Poppins:wght@700;800&family=Allura&display=swap">
<style>
  :root{
    --backdrop:#232323;
    --blue-top:#1f62c9;
    --blue-mid:#4a9ee0;
    --blue-deep:#163a78;
    --navy:#0f1f40;
    --card-top:#1f3f86;
    --card-bottom:#13264f;
    --white:#ffffff;
    --brand:#2b6cc4;
    --arrow:#111111;
    --photo-light:#d9dadb;
    --photo-dark:#6c6f73;
  }
  *{box-sizing:border-box;margin:0;padding:0}
  html,body{width:1200px;height:1200px;overflow:hidden;background:var(--backdrop)}
  .poster{
    position:absolute;left:201px;top:51px;width:798px;height:1097px;overflow:hidden;
    font-family:"Poppins",sans-serif;color:var(--white);
    background:
      radial-gradient(ellipse 380px 420px at 400px 560px, rgba(200,235,255,.85) 0%, rgba(110,185,240,.55) 35%, rgba(70,150,225,0) 70%),
      linear-gradient(180deg,var(--blue-top) 0%,var(--blue-mid) 38%,#3a86d0 60%,var(--blue-deep) 85%,var(--navy) 100%);
  }
  .brand-tab-ring{
    position:absolute;left:217px;top:-10px;width:363px;height:142px;
    background:#2d6ccc;border-radius:0 0 182px 182px / 0 0 110px 110px;
  }
  .brand-tab{
    position:absolute;left:234px;top:0;width:330px;height:122px;
    background:var(--white);border-radius:0 0 165px 165px / 0 0 95px 95px;
    display:flex;align-items:center;justify-content:center;gap:10px;padding-bottom:14px;
  }
  .brand-dot{width:18px;height:18px;border-radius:50%;background:var(--brand)}
  .brand-name{font-weight:800;font-size:31px;color:var(--brand);letter-spacing:.5px}
  .headline{position:absolute;font-weight:800;font-size:66px;line-height:1;letter-spacing:-1px}
  .headline.line-1{left:119px;top:146px}
  .headline.line-2{left:245px;top:205px}
  .dispenser-photo{
    position:absolute;left:153px;top:306px;width:491px;height:603px;
    background:linear-gradient(180deg,var(--photo-dark) 0%,#8a8d90 40%,var(--photo-light) 65%,#7a7d80 100%);
    border-radius:14px;opacity:.9;
  }
  .guide-card{
    position:absolute;border:3px solid var(--white);border-radius:16px;
    background:linear-gradient(160deg,var(--card-top),var(--card-bottom));
    display:flex;flex-direction:column;align-items:center;justify-content:flex-end;
    font-weight:700;text-align:center;line-height:1.05;
  }
  .guide-card svg{flex:none}
  .card-softener{left:97px;top:414px;width:140px;height:159px;padding-bottom:14px;font-size:21px}
  .card-bleach{left:566px;top:414px;width:139px;height:159px;padding-bottom:18px;font-size:22px}
  .card-detergent-left{left:39px;top:649px;width:127px;height:145px;padding-bottom:16px;font-size:18px}
  .card-detergent-right{left:636px;top:649px;width:127px;height:145px;padding-bottom:16px;font-size:18px}
  .arrows{position:absolute;left:0;top:0;width:798px;height:1097px;pointer-events:none}
  .pod-note{
    position:absolute;left:0;width:798px;top:955px;text-align:center;
    font-weight:700;font-size:28px;text-shadow:2px 2px 3px rgba(0,0,0,.7);
  }
  .sign-off{
    position:absolute;left:0;width:798px;top:1005px;text-align:center;
    font-family:"Allura",cursive;font-size:64px;line-height:1;
  }
</style>
</head>
<body>
<main class="poster">
  <div class="brand-tab-ring"></div>
  <div class="brand-tab"><span class="brand-dot"></span><span class="brand-name">SUDS HARBOR</span></div>

  <h1 class="headline line-1">where does</h1>
  <h1 class="headline line-2">the soap go?</h1>

  <div class="dispenser-photo" role="img" aria-label="Photo of the washer's open soap dispenser tray with four compartments: softener and bleach at the back, two detergent cups at the front"></div>

  <div class="guide-card card-softener">
    <svg width="76" height="76" viewBox="-40 -40 80 80" aria-hidden="true">
      <g fill="none" stroke="#fff" stroke-width="5">
        <ellipse cx="0" cy="-24" rx="6" ry="12"/>
        <ellipse cx="0" cy="-24" rx="6" ry="12" transform="rotate(45)"/>
        <ellipse cx="0" cy="-24" rx="6" ry="12" transform="rotate(90)"/>
        <ellipse cx="0" cy="-24" rx="6" ry="12" transform="rotate(135)"/>
        <ellipse cx="0" cy="-24" rx="6" ry="12" transform="rotate(180)"/>
        <ellipse cx="0" cy="-24" rx="6" ry="12" transform="rotate(225)"/>
        <ellipse cx="0" cy="-24" rx="6" ry="12" transform="rotate(270)"/>
        <ellipse cx="0" cy="-24" rx="6" ry="12" transform="rotate(315)"/>
      </g>
      <circle r="10" fill="#fff"/>
    </svg>
    <span>Fabric<br>Softener</span>
  </div>

  <div class="guide-card card-bleach">
    <svg width="100" height="80" viewBox="0 0 100 80" aria-hidden="true">
      <path d="M6 6 L12 40 H36 L42 6" fill="none" stroke="#fff" stroke-width="5"/>
      <path d="M24 12 C18 22 18 28 24 28 C30 28 30 22 24 12Z" fill="#fff"/>
      <line x1="66" y1="6" x2="30" y2="74" stroke="#fff" stroke-width="2.5"/>
      <path d="M68 34 L92 72 H44 Z" fill="none" stroke="#fff" stroke-width="6" stroke-linejoin="miter"/>
    </svg>
    <span>Bleach</span>
  </div>

  <div class="guide-card card-detergent-left">
    <svg width="70" height="62" viewBox="0 0 70 62" aria-hidden="true">
      <path d="M4 6 L14 56 H56 L66 6" fill="none" stroke="#fff" stroke-width="5"/>
      <line x1="35" y1="4" x2="35" y2="44" stroke="#fff" stroke-width="7"/>
    </svg>
    <span style="margin-top:14px">Detergent</span>
  </div>

  <div class="guide-card card-detergent-right">
    <svg width="70" height="62" viewBox="0 0 70 62" aria-hidden="true">
      <path d="M4 6 L14 56 H56 L66 6" fill="none" stroke="#fff" stroke-width="5"/>
      <line x1="29" y1="4" x2="29" y2="44" stroke="#fff" stroke-width="7"/>
      <line x1="41" y1="4" x2="41" y2="44" stroke="#fff" stroke-width="7"/>
    </svg>
    <span style="margin-top:14px">Detergent</span>
  </div>

  <svg class="arrows" viewBox="0 0 798 1097" aria-hidden="true">
    <g fill="none" stroke="var(--arrow)" stroke-width="4.5" stroke-linecap="round" stroke-linejoin="round">
      <path d="M179 586 C200 640 260 665 312 663"/>
      <path d="M296 650 L314 663 L298 678"/>
      <path d="M609 586 C590 630 540 660 481 666"/>
      <path d="M494 652 L479 666 L497 678"/>
      <path d="M183 769 C190 735 250 735 282 772"/>
      <path d="M264 770 L283 776 L286 756"/>
      <path d="M617 772 C610 738 555 738 516 772"/>
      <path d="M534 772 L515 776 L513 756"/>
    </g>
  </svg>

  <p class="pod-note">*Please place pods inside the washer</p>
  <p class="sign-off">Thanks</p>
</main>
</body>
</html>
```